Creative Challenge - Disruptive Digital Construction Business needs an Application Design

We need an application design (4 screens).
The app will offer easy-to-use an interactive course to illustrate the latest technology to construction professionals. Kindly find the attachments.
Updates

I have just posted the contest and the deadline is tomorrow!! Please give me my original 7 days back.

Need extra days to review

Target Market(s)

Construction professionals, aged from 22 to 36, who want to learn new disruptive technologies in construction.

Colors
e667a6
b868aa
33a6d7

Requirements
Must have
• The name of the app, Velunor, stands for “Brightframe Skill Voyagers”. The user is a Velunor, who would transform the digital construction industry. We want a design that gives that feel to the users.

```html
<!DOCTYPE html>
<html lang="en">
<head>
<meta charset="utf-8">
<title>Velunor – Onboarding</title>
<link href="https://fonts.googleapis.com/css2?family=Roboto:wght@400;500;700&display=swap" rel="stylesheet">
<style>
  :root {
    --page-bg: #ffffff;
    --screen-bg: #ffffff;
    --ink: #222222;
    --body-text: #555555;
    --pink: #e2478f;
    --blue: #2b9fd5;
    --purple: #b14fa0;
    --button: #33a6d7;
    --button-glow: rgba(51, 166, 215, 0.35);
    --card-shadow: rgba(0, 0, 0, 0.10);
    --screen-shadow: rgba(0, 0, 0, 0.12);
  }
  * { box-sizing: border-box; margin: 0; padding: 0; }
  html, body {
    width: 1200px; height: 1000px; overflow: hidden;
    background: var(--page-bg);
    font-family: "Roboto", Arial, sans-serif;
  }
  .screen {
    position: absolute; left: 390px; top: 45px;
    width: 420px; height: 910px;
    background: var(--screen-bg);
    box-shadow: 0 10px 40px var(--screen-shadow);
  }
  .status-bar {
    position: absolute; left: 16px; right: 16px; top: 15px; height: 16px;
    display: flex; justify-content: space-between; align-items: center;
    font-size: 12px; color: var(--ink);
  }
  .status-left, .status-right { display: flex; align-items: center; gap: 5px; }
  .hero-card {
    position: absolute; left: 37px; top: 117px;
    width: 346px; height: 318px; border-radius: 46px;
    background: #ffffff;
    box-shadow: 0 12px 30px var(--card-shadow);
  }
  .hero-illustration {
    position: absolute; left: 36px; top: 53px;
    width: 274px; height: 213px; border-radius: 10px;
    background: linear-gradient(180deg, #f2f2f4 0%, #e7e6f6 55%, #f6f6f8 100%);
  }
  .intro {
    position: absolute; left: 0; right: 0; top: 486px;
    text-align: center;
    font-size: 20px; line-height: 32px; color: var(--body-text);
  }
  .meta {
    position: absolute; left: 0; right: 0; top: 568px;
    text-align: center; font-size: 20px; line-height: 37px;
  }
  .meta-level { color: var(--pink); }
  .meta-stage { color: var(--blue); }
  .meta-actor { color: var(--purple); }
  .cta {
    position: absolute; left: 39px; top: 767px;
    width: 343px; height: 67px; border-radius: 3px;
    background: var(--button); color: #ffffff;
    font-size: 17px; font-weight: 700;
    display: flex; align-items: center; justify-content: center;
    box-shadow: 0 18px 36px var(--button-glow);
  }
</style>
</head>
<body>
  <main class="screen">
    <div class="status-bar">
      <div class="status-left">
        <svg width="44" height="8" viewBox="0 0 44 8" aria-hidden="true">
          <circle cx="4" cy="4" r="3.2" fill="#222"/>
          <circle cx="12" cy="4" r="3.2" fill="#222"/>
          <circle cx="20" cy="4" r="3.2" fill="#222"/>
          <circle cx="28" cy="4" r="2.8" fill="none" stroke="#222" stroke-width="0.8"/>
          <circle cx="36" cy="4" r="2.8" fill="none" stroke="#222" stroke-width="0.8"/>
        </svg>
        <span>GS</span>
        <svg width="14" height="11" viewBox="0 0 14 11" aria-hidden="true">
          <path d="M1 4 A9 9 0 0 1 13 4" fill="none" stroke="#222" stroke-width="1.6"/>
          <path d="M3.5 6.5 A5.5 5.5 0 0 1 10.5 6.5" fill="none" stroke="#222" stroke-width="1.6"/>
          <circle cx="7" cy="9.3" r="1.4" fill="#222"/>
        </svg>
      </div>
      <div class="status-right">
        <span>58 %</span>
        <svg width="27" height="12" viewBox="0 0 27 12" aria-hidden="true">
          <rect x="0.5" y="0.5" width="23" height="11" rx="2" fill="none" stroke="#222"/>
          <rect x="2" y="2" width="11" height="8" fill="#222"/>
          <rect x="24.5" y="4" width="2" height="4" fill="#222"/>
        </svg>
      </div>
    </div>

    <section class="hero-card">
      <div class="hero-illustration" role="img" aria-label="Line illustration of an office building with purple windows between two trees and a pink sun"></div>
    </section>

    <p class="intro">Nominate Individuals to undertake the<br>information management function</p>

    <div class="meta">
      <p class="meta-level">Appointment Level</p>
      <p class="meta-stage">Information Procurement Stage</p>
      <p class="meta-actor">Actor: The Lead Appointed Party</p>
    </div>

    <div class="cta">Get Started with Velunor</div>
  </main>
</body>
</html>
```